Inspire Design with Natural Stone: Quarrell Ltd. Tradeshow Booth Backdrop

Client: Quarrell Ltd.
Project Goal: To design a visually compelling and informative 7.5ft x 10ft backdrop for Quarrell Ltd.'s 10ft x 10ft tradeshow booth that attracts and engages architects, designers, homeowners, and contractors, ultimately driving interest in their natural stone products.
Quarrell Ltd. is a leading provider of high-quality natural stone for a wide range of residential and commercial projects. We offer a diverse selection of stone types, finishes, and applications, known for their beauty, durability, and timeless appeal. We are participating in upcoming tradeshows to generate new leads, strengthen brand awareness, and showcase our latest offerings to key target audiences.
Target Audience(s):
Architects: Seeking premium, unique, and sustainable natural stone options for their designs, with an appreciation for quality and aesthetic integration.
Designers (Interior & Landscape): Looking for visually appealing and versatile stone to enhance their projects, focusing on texture, color palettes, and application possibilities.
Homeowners: Aspiring to elevate their living spaces with natural stone, driven by aesthetics, durability, and adding lasting value to their homes.
Contractors: Seeking reliable and high-quality stone suppliers for their building and renovation projects, prioritizing ease of installation and client satisfaction.
Key Message/Desired Outcome: We want our booth to communicate that Quarrell Ltd. is the premier source for beautiful, high-quality natural stone solutions for any project, backed by expertise and a commitment to customer satisfaction. We want to inspire visitors with the possibilities of using natural stone in their designs and projects.
Mandatories:
* Backdrop Dimensions: 7.5 feet (height) x 10 feet (width). (See attached template)
* Inclusion of Quarrell Ltd. Logo:* The logo must be prominently featured and easily recognizable. Please refer to the attached brand guidelines for logo usage, color palette, and typography.
*Clear Representation of Natural Stone: The design must showcase the beauty and variety of Quarrell Ltd.'s natural stone products. This can be achieved through high-quality photography, subtle textures, or artistic representations. Please use our website's photo and project gallery.
*Contact Information: Include our website address: www.quarrellbrix.example
Optional Elements (Consideration):
*Visuals of Applications: Showcasing natural stone used in various settings (e.g., fireplaces, facades, patios, interior walls) could be impactful.
*Highlighting Key Benefits: Briefly communicating the advantages of natural stone (e.g., durability, sustainability, timelessness).
*Integration of Textures: Subtly incorporating textures that hint at the feel of natural stone.
Look and Feel:
*Overall Impression: Sophisticated, natural, high-quality, inviting, trustworthy, and inspiring.
*Style: Clean, modern, and visually appealing, allowing the beauty of the stone to take center stage. Avoid overly busy or cluttered designs.
*Color Palette: Primarily utilize Quarrell Ltd.'s brand colors (refer to brand guidelines).
Things to Avoid:
* Generic stock imagery that doesn't accurately represent Quarrell's products.
* Cluttered layouts with excessive text.
* Designs that appear cheap or unprofessional.
* Difficult-to-read fonts or color combinations.
Deliverables:
* High-resolution digital design file(s) suitable for large-format printing (AI, Photoshop, PDF).
* Mockup of the backdrop design within a 10ft x 10ft booth space. Please feel free to include any other booth features (tables, flooring, etc) that you think would work well with the backdrop (optional but highly recommended).
We are excited to see your creative interpretations and look forward to selecting a design that will make a strong and lasting impression at our upcoming tradeshows!

```html
<!DOCTYPE html>
<html lang="en">
<head>
<meta charset="utf-8">
<title>Quarrell Ltd. Tradeshow Backdrop</title>
<link href="https://fonts.googleapis.com/css2?family=Saira:wght@500;600&display=swap" rel="stylesheet">
<style>
  :root {
    --navy: #1b2a3d;
    --navy-deep: #121d2b;
    --navy-light: #2a3c53;
    --white: #f4f4f2;
    --wood: #6b4a2e;
    --wall: #cfc6b6;
    --stone: #9c8b72;
    --floor: #8a5a34;
  }
  html, body {
    margin: 0;
    padding: 0;
    width: 1200px;
    height: 857px;
    overflow: hidden;
    background: #ffffff;
  }
  .backdrop {
    position: relative;
    width: 1200px;
    height: 857px;
    overflow: hidden;
    font-family: "Saira", "Segoe UI", sans-serif;
    color: var(--white);
    background: var(--navy);
  }
  .scene-photo {
    position: absolute;
    top: 0;
    right: 0;
    width: 780px;
    height: 857px;
    background:
      linear-gradient(180deg, var(--wood) 0%, #7a5a3c 15%, var(--wall) 28%, #d6cdbd 60%, #a7835d 82%, var(--floor) 100%);
  }
  .scene-photo::after {
    content: "";
    position: absolute;
    left: 300px;
    top: 0;
    width: 240px;
    height: 100%;
    background: linear-gradient(180deg, #a8957a 0%, var(--stone) 50%, #b3a184 100%);
    opacity: 0.85;
  }
  .brand-panel {
    position: absolute;
    inset: 0;
    background:
      radial-gradient(ellipse at 25% 30%, var(--navy-light) 0%, transparent 55%),
      linear-gradient(90deg, var(--navy-deep) 0%, var(--navy) 42%, rgba(27,42,61,0.85) 52%, rgba(27,42,61,0) 68%);
  }
  .brand-mark {
    position: absolute;
    left: 108px;
    top: 120px;
    display: flex;
    align-items: center;
    gap: 14px;
    font-size: 38px;
    font-weight: 500;
    letter-spacing: 1px;
    color: var(--white);
  }
  .brand-mark .mark-square {
    width: 26px;
    height: 26px;
    background: var(--white);
  }
  .headline {
    position: absolute;
    left: 108px;
    top: 262px;
    margin: 0;
    font-weight: 600;
    line-height: 1;
    color: var(--white);
  }
  .headline span { display: block; }
  .headline .line-craft { font-size: 128px; letter-spacing: 1px; }
  .headline .line-vision { font-size: 56px; font-weight: 500; margin-top: 2px; }
  .headline .line-stone { font-size: 120px; letter-spacing: 2px; margin-top: -2px; }
  .web-address {
    position: absolute;
    left: 106px;
    top: 650px;
    font-size: 42px;
    font-weight: 600;
  }
  .web-address-vertical {
    position: absolute;
    left: 8px;
    top: 430px;
    transform: translate(-50%, -50%) rotate(-90deg) translateY(28px);
    transform-origin: center;
    font-size: 34px;
    font-weight: 600;
    white-space: nowrap;
  }
</style>
</head>
<body>
  <main class="backdrop">
    <div class="scene-photo" role="img" aria-label="Living room with a tall natural stone fireplace, wooden beam ceiling, mantel and warm wood floor"></div>
    <div class="brand-panel"></div>

    <div class="brand-mark">
      <span class="mark-square"></span>
      <span class="mark-name">QUARRELL</span>
    </div>

    <h1 class="headline">
      <span class="line-craft">CRAFT</span>
      <span class="line-vision">YOUR VISION IN</span>
      <span class="line-stone">STONE</span>
    </h1>

    <div class="web-address">quarrellbrix.example</div>
    <div class="web-address-vertical">quarrellbrix.example</div>
  </main>
</body>
</html>
```